Kestrel Ridgeway LLC stationery, business card and web page design.

i need a full set of stationery designed using the name "Kestrel Ridgeway LLC" with a tag line "construction consulting services". using the uploaded monkey icon as the logo.

i like the colors orange, green and black in general but im not limited to that. the company offers consulting services to various types of construction businesses.

Target Market(s)

i travel around the country in a 4x4 camper offering consulting services and technical training short term and long to various types of construction companies.

Industry/Entity Type

Construction Company

Contact Information for Business Card

Martin Hale
m.hale@kestrelridgeway.example
2475 Birchfield Rd
Bohemia, NY 11716
555 314 0627

list these services on the card.

Business Consulting
Capital Investments
Marketing Implementations
Technical Training

Number of Pages Required

1 page

Colors

Designer to choose colors to be used in the design.

Requirements
Must have
• company info and use of the monkey icon i provided.
Nice to have
• a fun but professional design
Should not have
• the color red

```html
<!DOCTYPE html>
<html lang="en">
<head>
<meta charset="utf-8">
<title>Kestrel Ridgeway LLC – Business Card</title>
<link rel="stylesheet" href="https://fonts.googleapis.com/css2?family=Cinzel:wght@400;600&family=Roboto:wght@400&display=swap">
<style>
  :root {
    --canvas: #e9e6e1;
    --orange: #f15a22;
    --ink: #111111;
    --muted: #444444;
    --paper: #f3f3f3;
    --mascot-black: #0d0d0d;
  }
  * { margin: 0; padding: 0; box-sizing: border-box; }
  html, body { width: 1200px; height: 960px; overflow: hidden; background: var(--canvas); }
  .canvas { position: relative; width: 1200px; height: 960px; }

  .card {
    position: absolute; left: 300px; width: 598px; height: 341px;
    border-radius: 22px; overflow: hidden;
    box-shadow: 0 3px 8px rgba(0,0,0,.25);
  }
  .card--front { top: 137px; background: var(--orange); }
  .card--back { top: 489px; background: var(--paper); }

  .mascot-area { position: absolute; left: 0; top: 0; width: 340px; height: 341px; }

  .serif { font-family: "Cinzel", "Times New Roman", serif; color: var(--ink); text-transform: uppercase; }
  .sans { font-family: "Roboto", Arial, sans-serif; color: var(--ink); }

  .front-info { position: absolute; right: 32px; text-align: right; white-space: nowrap; }
  .person-name { top: 37px; font-size: 24px; line-height: 1; }
  .person-role { top: 63px; font-size: 14px; line-height: 1; font-weight: 600; }
  .address { top: 91px; font-size: 14px; line-height: 18px; }

  .contact-list { position: absolute; right: 32px; top: 156px; list-style: none; }
  .contact-list li {
    display: flex; justify-content: flex-end; align-items: center;
    font-family: "Roboto", Arial, sans-serif; font-size: 14px; line-height: 19.5px; color: var(--ink);
  }
  .contact-list svg { width: 12px; height: 12px; margin-left: 9px; fill: var(--ink); }

  .company-name { top: 266px; font-size: 21px; line-height: 1; }
  .company-tagline { top: 293px; font-size: 12px; line-height: 1; }

  .brand-mark {
    position: absolute; left: 50%; top: 58px; width: 150px; height: 150px;
    transform: translateX(-50%); border-radius: 50%; background: var(--mascot-black);
  }
  .back-name {
    position: absolute; width: 100%; top: 244px; text-align: center;
    font-size: 24px; color: var(--orange); line-height: 1;
  }
  .back-tagline {
    position: absolute; width: 100%; top: 273px; text-align: center; font-size: 14px; line-height: 1;
  }
  .service-list {
    position: absolute; width: 100%; top: 300px; list-style: none;
    display: flex; justify-content: center; gap: 0;
    font-family: "Roboto", Arial, sans-serif; font-size: 11px; line-height: 1; color: var(--muted);
  }
  .service-list li + li::before { content: "•"; color: var(--orange); margin: 0 8px; }
</style>
</head>
<body>
<main class="canvas">
  <section class="card card--front">
    <svg class="mascot-area" viewBox="0 0 340 341" role="img" aria-label="Mascot illustration: large cartoon monkey head in black and white">
      <path d="M0 0 H248 C300 80 300 250 196 341 H0 Z" fill="var(--mascot-black)"/>
    </svg>

    <p class="front-info serif person-name">Martin Hale</p>
    <p class="front-info serif person-role">CEO/Founder</p>
    <p class="front-info sans address">Kestrel Ridgeway LLC<br>2475 Birchfield Rd<br>Bohemia, NY 11716</p>

    <ul class="contact-list">
      <li>555 314 0627<svg viewBox="0 0 24 24"><path d="M6.6 10.8a15 15 0 0 0 6.6 6.6l2.2-2.2c.3-.3.7-.4 1-.2 1.1.4 2.3.6 3.6.6.6 0 1 .4 1 1V20c0 .6-.4 1-1 1A17 17 0 0 1 3 4c0-.6.4-1 1-1h3.5c.6 0 1 .4 1 1 0 1.3.2 2.5.6 3.6.1.3 0 .7-.2 1z"/></svg></li>
      <li>555 314 0628<svg viewBox="0 0 24 24"><path d="M7 1h10a2 2 0 0 1 2 2v18a2 2 0 0 1-2 2H7a2 2 0 0 1-2-2V3a2 2 0 0 1 2-2zm0 3v14h10V4z"/></svg></li>
      <li>555 314 0629<svg viewBox="0 0 24 24"><path d="M6 2h12v6H6zM3 9h18a1 1 0 0 1 1 1v8h-4v4H6v-4H2v-8a1 1 0 0 1 1-1zm5 8v3h8v-3z"/></svg></li>
      <li>m.hale@kestrelridgeway.example<svg viewBox="0 0 24 24"><path d="M2 5h20v2l-10 6L2 7zm0 4l10 6 10-6v10H2z"/></svg></li>
      <li>www.kestrelridgeway.example<svg viewBox="0 0 24 24"><circle cx="12" cy="12" r="10"/></svg></li>
    </ul>

    <p class="front-info serif company-name">Kestrel Ridgeway LLC</p>
    <p class="front-info serif company-tagline">Construction Consulting Services</p>
  </section>

  <section class="card card--back">
    <div class="brand-mark"></div>
    <p class="serif back-name">Kestrel Ridgeway LLC</p>
    <p class="serif back-tagline">Construction Consulting Services</p>
    <ul class="service-list">
      <li>Business Consulting</li>
      <li>Capital Investments</li>
      <li>Marketing Implementations</li>
      <li>Technical Training</li>
    </ul>
  </section>
</main>
</body>
</html>
```